" Somos uma empresa de assessoria e consultoria em gestão da qualidade e segurança dos alimentos. Nossa equipe é formada por engenheiros de alimentos. E a prestação de serviço realizada pela Vorunt compreende: a) Auditorias diagnósticas dos sistemas de qualidade e segurança dos alimentos, ou seja, avaliação do status atual do cliente, de acordo com a legislação sanitária (órgãos de vigilância sanitária, como por ex. SEPROL e Junta Federal de Colheitas) ou de acordo com as exigências de com normas reconhecidas internacionalmente, pelo setor alimentício, como por exemplo NTQ 48100, Verdal KMT; b) Auditorias de conformidade dos sistemas de qualidade e segurança dos alimentos, ou seja, avaliação do status do cliente, após correção das não conformidades apontadas na auditoria diagnóstica, de acordo com a legislação sanitária (órgãos de vigilância sanitária, como por ex. SEPROL e Junta Federal de Colheitas) ou de acordo com as exigências de com normas reconhecidas internacionalmente, pelo setor alimentício, como por exemplo NTQ 48100, Verdal KMT; c) Auditorias Internas dos Sistemas de Qualidade e Segurança de limentos, onde é verificado a implementação e manutenção dos Sistemas de Qualidade e Segurança dos Alimentos; d) Elaboração de documentos referentes à qualidade e segurança de alimentos, exigidos pela legislação sanitária em vigor no Brasil e/ou legislação sanitária de outros países e/ou àquelas exigidas por normas internacionais; e) Implantação de Sistemas de Qualidade e Segurança dos Alimentos, de acordo com a legislação sanAitária em vigor no Brasil e/ou legislação sanitária de outros países e/ou normas internacionais; f) Capacitação de profissionais de nível gerencial ou de supervisão, assim como também manipuladores de alimentos diretos ou indiretos, em temas relacionados à qualidade e segurança dos alimentos; g) Comercio eletrônico (atividade futura) de produtos relacionados à sistema de qualidade e segurança dos alimentos, como por exemplo: instrumentos de medição (termômetros, por exemplo), equipamentos de proteção individual (EPIs), sinalizadores educativos, entre outros. O método utilizado para a comercialização será por meio de representação de fabricantes destes produtos. "

```html
<!DOCTYPE html>
<html lang="pt-BR">
<head>
<meta charset="utf-8">
<title>Vorunt — Cartão de visita</title>
<link href="https://fonts.googleapis.com/css2?family=Roboto:wght@400;500;700;900&display=swap" rel="stylesheet">
<style>
  :root {
    --bg: #e6e7ea;
    --card: #ffffff;
    --ink: #2b2e3a;
    --text: #4a4d57;
    --red: #d7202b;
  }
  * { box-sizing: border-box; margin: 0; padding: 0; }
  html, body { width: 1200px; height: 1200px; overflow: hidden; }
  body {
    background: var(--bg);
    font-family: "Roboto", Arial, sans-serif;
    position: relative;
  }
  .card {
    position: absolute;
    left: 170px;
    width: 860px;
    height: 478px;
    background: var(--card);
    box-shadow: 0 6px 18px rgba(0,0,0,0.12);
    overflow: hidden;
  }
  .card-front { top: 90px; }
  .card-back { top: 630px; }
  .card-band {
    position: absolute;
    left: 0; right: 0; bottom: 0;
    height: 30px;
    background: var(--red);
  }
  .card-band::before {
    content: "";
    position: absolute;
    left: 0; right: 0; top: 6px;
    height: 3px;
    background: var(--card);
  }
  /* Front */
  .brand-block {
    position: absolute;
    left: 150px; top: 150px;
    display: flex;
    flex-direction: column;
    align-items: flex-end;
    gap: 14px;
  }
  .brand {
    display: flex; align-items: center; gap: 18px;
  }
  .brand-dot {
    width: 62px; height: 62px;
    border-radius: 50%;
    background: var(--red);
  }
  .brand-name {
    font-weight: 900;
    font-size: 96px;
    letter-spacing: 4px;
    color: var(--ink);
    line-height: 1;
  }
  .brand-tagline {
    font-weight: 700;
    font-size: 24px;
    color: var(--red);
    white-space: nowrap;
  }
  /* Back */
  .holder {
    position: absolute;
    left: 60px; top: 56px;
    display: flex; align-items: center; gap: 18px;
  }
  .holder-name {
    font-weight: 700;
    font-size: 38px;
    color: var(--ink);
  }
  .holder-role {
    position: absolute;
    left: 240px; top: 108px;
    font-size: 18px;
    letter-spacing: 1px;
    color: var(--text);
  }
  .contact-list {
    position: absolute;
    left: 60px; top: 160px;
    list-style: none;
  }
  .contact-item {
    display: flex; align-items: flex-start; gap: 22px;
    margin-bottom: 22px;
    font-size: 19px;
    line-height: 1.35;
    color: var(--text);
  }
  .contact-icon { width: 30px; height: 30px; flex: none; }
</style>
</head>
<body>

<section class="card card-front">
  <div class="brand-block">
    <div class="brand">
      <span class="brand-dot"></span>
      <span class="brand-name">VORUNT</span>
    </div>
    <p class="brand-tagline">Segurança e excelência para o seu alimento!</p>
  </div>
  <div class="card-band"></div>
</section>

<section class="card card-back">
  <div class="holder">
    <svg class="contact-icon" viewBox="0 0 30 30" aria-hidden="true">
      <circle cx="15" cy="15" r="15" fill="var(--ink)"/>
      <circle cx="15" cy="11" r="5" fill="#fff"/>
      <path d="M6 24 a9 8 0 0 1 18 0 z" fill="#fff"/>
    </svg>
    <h1 class="holder-name">Marina Tavares da Costa</h1>
  </div>
  <p class="holder-role">DIRETORA EXECUTIVA</p>

  <ul class="contact-list">
    <li class="contact-item">
      <svg class="contact-icon" viewBox="0 0 30 30" aria-hidden="true">
        <circle cx="15" cy="15" r="15" fill="var(--ink)"/>
        <g fill="none" stroke="#fff" stroke-width="1.6">
          <circle cx="15" cy="15" r="8"/>
          <ellipse cx="15" cy="15" rx="3.5" ry="8"/>
          <line x1="7" y1="15" x2="23" y2="15"/>
        </g>
      </svg>
      <span>www.voruntconsultoria.com.br</span>
    </li>
    <li class="contact-item">
      <svg class="contact-icon" viewBox="0 0 30 30" aria-hidden="true">
        <circle cx="15" cy="15" r="15" fill="var(--ink)"/>
        <rect x="11" y="7" width="8" height="16" rx="1.5" fill="#fff"/>
        <rect x="12.5" y="9" width="5" height="10" fill="var(--ink)"/>
      </svg>
      <span>+55 11 94731-2058</span>
    </li>
    <li class="contact-item">
      <svg class="contact-icon" viewBox="0 0 30 30" aria-hidden="true">
        <circle cx="15" cy="15" r="15" fill="var(--ink)"/>
        <rect x="8" y="10" width="14" height="10" fill="#fff"/>
        <path d="M8 10 l7 6 l7 -6" fill="none" stroke="var(--ink)" stroke-width="1.4"/>
      </svg>
      <span>marina@voruntconsultoria.com.br</span>
    </li>
    <li class="contact-item">
      <svg class="contact-icon" viewBox="0 0 30 30" aria-hidden="true">
        <circle cx="15" cy="15" r="15" fill="var(--ink)"/>
        <path d="M15 24 C10 17 9.5 15 9.5 12.5 a5.5 5.5 0 0 1 11 0 C20.5 15 20 17 15 24z" fill="#fff"/>
        <circle cx="15" cy="12.5" r="2" fill="var(--ink)"/>
      </svg>
      <span>Rua das Acácias 742 - CJ 58 - Edifício Horizonte - Lapa<br>CEP 05074-120 - São Paulo - SP</span>
    </li>
  </ul>
  <div class="card-band"></div>
</section>

</body>
</html>
```